Business Card Design Project

Business Card
We are rebranding with a new logo
Industry/Entity Type
Business
Contact Information for Business Card
Dennis Marlow +61 427581962 dennis@qovo.com.au P.O. Box 872 Kelvindale QLD 4309
Requirements
Must have
- Logo

```html
<!DOCTYPE html>
<html lang="en">
<head>
<meta charset="utf-8">
<title>Qovo International – Business Card</title>
<link rel="stylesheet" href="https://fonts.googleapis.com/css2?family=Libre+Baskerville:wght@400;700&display=swap">
<style>
  :root {
    --page-bg: #e6e6e6;
    --card-bg: #ffffff;
    --brand-blue: #2a8cc4;
    --brand-orange: #f08324;
    --ink: #1c1c1c;
    --band-dark: #1a1a1a;
  }
  * { box-sizing: border-box; margin: 0; padding: 0; }
  html, body {
    width: 1200px; height: 1000px; overflow: hidden;
    background: var(--page-bg);
    font-family: "Libre Baskerville", "Book Antiqua", Georgia, serif;
    color: var(--ink);
  }
  .business-card {
    position: absolute; left: 250px; top: 300px;
    width: 700px; height: 400px;
    background: var(--card-bg);
    border-radius: 28px;
    overflow: hidden;
    box-shadow: 0 10px 30px rgba(0,0,0,0.15);
  }
  .brand {
    position: absolute; left: 70px; top: 92px;
    display: flex; align-items: center; gap: 14px;
  }
  .brand-dot {
    width: 34px; height: 34px; border-radius: 50%;
    background: var(--brand-orange);
  }
  .brand-name {
    font-weight: 700; font-size: 30px; letter-spacing: 2px;
    color: var(--brand-blue); line-height: 1.1;
  }
  .divider {
    position: absolute; left: 70px; right: 40px; top: 200px;
    height: 1.5px; background: var(--brand-orange);
  }
  .holder {
    position: absolute; right: 40px; top: 140px; text-align: right;
  }
  .holder-name {
    font-weight: 700; font-size: 22px; letter-spacing: 1px; text-transform: uppercase;
  }
  .holder-role {
    font-size: 16px; color: var(--brand-orange); margin-top: 2px;
  }
  .postal-address {
    position: absolute; right: 40px; top: 218px;
    text-align: right; font-weight: 700; font-size: 15px;
    line-height: 1.55; letter-spacing: 1px; font-style: normal;
  }
  .contact-list {
    position: absolute; left: 70px; top: 290px; list-style: none;
  }
  .contact-item {
    display: flex; align-items: center; gap: 10px;
    font-weight: 700; font-size: 16px; margin-bottom: 8px;
  }
  .contact-icon { width: 20px; height: 18px; flex: none; }
  .edge-band {
    position: absolute; left: 0; right: 0; bottom: 0; height: 30px;
    background: var(--brand-orange);
    border-top: 6px solid var(--band-dark);
  }
</style>
</head>
<body>
  <section class="business-card">
    <div class="brand">
      <span class="brand-dot"></span>
      <span class="brand-name">QOVO INTERNATIONAL</span>
    </div>

    <div class="holder">
      <p class="holder-name">Dennis Marlow</p>
      <p class="holder-role">Founder</p>
    </div>

    <div class="divider"></div>

    <address class="postal-address">
      P.O. Box 872 Kelvindale<br>QLD 4309
    </address>

    <ul class="contact-list">
      <li class="contact-item">
        <svg class="contact-icon" viewBox="0 0 20 18" aria-hidden="true">
          <rect x="1" y="1" width="18" height="16" rx="6" fill="none" stroke="var(--brand-orange)" stroke-width="2"/>
          <rect x="7" y="4" width="6" height="10" rx="1" fill="var(--brand-orange)"/>
        </svg>
        +61 427581962
      </li>
      <li class="contact-item">
        <svg class="contact-icon" viewBox="0 0 20 18" aria-hidden="true">
          <rect x="1" y="1" width="18" height="16" rx="6" fill="none" stroke="var(--brand-orange)" stroke-width="2"/>
          <rect x="5" y="5" width="10" height="8" fill="var(--brand-orange)"/>
          <path d="M5 5 L10 10 L15 5" fill="none" stroke="#fff" stroke-width="1.3"/>
        </svg>
        dennis@qovo.com.au
      </li>
    </ul>

    <div class="edge-band"></div>
  </section>
</body>
</html>
```